Supplement Label Design - Sports Nutrition

Design a sports nutrition/weight loss supplement label that stands out in a crowded space. Supplement bottle size is 200c and label size is 7" x 2.5" approximately. We're looking for a design that emphasizes the products name called VYK. Vyk is an abbreviation for Vigor, Yield & Kinetics. We want VYK to be the center/focus point of the bottle and have a memorable design to it.

Target Market(s)

Men & Women over 18

Industry/Entity Type

Supplement

Font styles to use
Sans Serif
Decorative

Requirements
Must have
• Emphasis on the product name VYK. Serious, Inspirational & Motivational feel to the design, typo & colors. Electrocution/lightning feel to the text. Right hand side of label is our formulation. Left hand side is dedicated to explaining the trifecta formulation idea.
Nice to have
• For example, we like the graphic design of "Drum" energy drinks because you can identify the bottle from a distance and is memorable. We think that less is more and we'd like the design/colors do most of the talking.
Should not have
• Cartroon/animated style.

```html
<!DOCTYPE html>
<html lang="en">
<head>
<meta charset="utf-8">
<title>VYK Sports Nutrition Supplement Label</title>
<link rel="stylesheet" href="https://fonts.googleapis.com/css2?family=Barlow:wght@500;600;800&family=Bangers&family=Arimo&display=swap">
<style>
  :root {
    --backdrop: #6b6b6b;
    --label-black: #111111;
    --label-sheen: #1c1c1c;
    --brand-red: #d8141a;
    --text-white: #f4f4f4;
    --gold-dark: #c9a24a;
    --gold-light: #f3e6a8;
    --ink: #1a1a1a;
  }
  * { margin: 0; padding: 0; box-sizing: border-box; }
  html, body {
    width: 1200px;
    height: 1103px;
    overflow: hidden;
    background: var(--backdrop);
  }
  .label {
    position: absolute;
    left: 397px;
    top: 170px;
    width: 408px;
    height: 740px;
    background: linear-gradient(90deg, var(--label-black) 0%, var(--label-sheen) 50%, var(--label-black) 100%);
    border-radius: 6px;
    overflow: hidden;
    text-align: center;
  }
  .maker {
    position: absolute;
    top: 140px;
    left: 0;
    width: 100%;
    font-family: "Barlow", sans-serif;
    font-weight: 500;
    font-size: 38px;
    letter-spacing: 1px;
    color: var(--text-white);
  }
  .product-name {
    position: absolute;
    top: 205px;
    left: 0;
    width: 100%;
    font-family: "Barlow", sans-serif;
    font-weight: 800;
    font-size: 210px;
    line-height: 1;
    letter-spacing: 4px;
    color: var(--brand-red);
  }
  .tagline-band {
    position: absolute;
    top: 502px;
    left: 0;
    width: 100%;
    height: 56px;
    background: linear-gradient(90deg, var(--gold-dark) 0%, var(--gold-light) 35%, #e8cf7a 65%, var(--gold-light) 100%);
    display: flex;
    align-items: center;
    justify-content: center;
  }
  .tagline {
    font-family: "Barlow", sans-serif;
    font-weight: 600;
    font-size: 23px;
    letter-spacing: 1px;
    color: var(--ink);
    text-transform: uppercase;
  }
  .category {
    position: absolute;
    top: 592px;
    left: 0;
    width: 100%;
    font-family: "Bangers", sans-serif;
    font-size: 30px;
    letter-spacing: 1.5px;
    color: var(--brand-red);
  }
  .flavor-note {
    position: absolute;
    top: 655px;
    left: 0;
    width: 100%;
    font-family: "Arimo", sans-serif;
    font-size: 26px;
    color: var(--text-white);
  }
</style>
</head>
<body>
  <main class="label">
    <p class="maker">Calorvance</p>
    <h1 class="product-name">VYK</h1>
    <div class="tagline-band">
      <p class="tagline">Vigor, Yield &amp; Kinetics</p>
    </div>
    <p class="category">SPORTS NUTRITION SUPPLEMENT</p>
    <p class="flavor-note">NATURAL FLAVORS</p>
  </main>
</body>
</html>
```